Business Card Design Project

We need a business card design for our company kV7 s.r.o. The company is based in Slovakia and selling massage, yoga and meditation accessories online and offline. At the place where the offices are, we have a yoga studio, massage room, show room and shop as well. We will give the business card for customers who visit our shop or show room personally and for the new suppliers of demanded products we are visiting in the future.
I would like to have:
- small logo and datas on one side
- big logo and our main e-shops on the other side:
- www.pohodanoviny.sk
- www.relaxbrodeky.cz
Datas:
Peter Hulka, MSc. / CEO
kV7 s.r.o.
Brezovanská 742/3
931 05 Lipová Dolina
Central Europe (EU)
Office tel.: +421 (0) 947 618 204
Private tel.: +421 (0) 907 251 836
E-mail: info@kv7example.sk
Web: www.kv7example.sk
It is up to you if you use graphics emphasizing our profile or leave it simple and modern without pics. Looking forward to receiving your designs! Thank You!
Industry/Entity Type
Massage
Colors
Designer to choose colors to be used in the design.
Look and feel
Each slider illustrates characteristics of the customer's brand and the style your logo design should communicate.

```html
<!DOCTYPE html>
<html lang="sk">
<head>
<meta charset="utf-8">
<title>kV7 s.r.o. – business card</title>
<link rel="stylesheet" href="https://fonts.googleapis.com/css2?family=Lato:wght@400;700;900&display=swap">
<style>
  :root {
    --backdrop: #2b2b2b;
    --paper: #f7f7f7;
    --ink: #3b3f45;
    --slate: #4a5565;
    --orange: #e8731f;
  }
  html, body {
    margin: 0;
    width: 1200px;
    height: 997px;
    overflow: hidden;
    background: var(--backdrop);
    font-family: "Lato", Arial, sans-serif;
    color: var(--ink);
  }
  .card {
    position: absolute;
    left: 280px;
    width: 640px;
    height: 366px;
    background: var(--paper);
    box-shadow: 0 12px 30px rgba(0,0,0,.5);
    overflow: hidden;
  }
  .card--back { top: 90px; }
  .card--front { top: 540px; }
  .card__bands { position: absolute; left: 0; bottom: 0; width: 640px; height: 366px; }
  .wordmark {
    position: absolute;
    font-weight: 900;
    color: var(--slate);
    letter-spacing: -1px;
    line-height: 1;
  }
  .card--back .wordmark { left: 60px; top: 130px; font-size: 64px; }
  .card--front .wordmark { left: 40px; top: 60px; font-size: 44px; }

  .eshops {
    position: absolute;
    left: 240px; top: 110px;
    font-weight: 900;
    font-size: 19px;
    letter-spacing: 1px;
    text-transform: uppercase;
    line-height: 38px;
    white-space: nowrap;
  }
  .tagline {
    position: absolute;
    left: 240px; top: 228px;
    color: var(--orange);
    font-size: 13px;
    letter-spacing: 3px;
    text-transform: uppercase;
    white-space: nowrap;
  }

  .person {
    position: absolute;
    right: 40px; top: 38px;
    text-align: right;
  }
  .person__name { color: var(--orange); font-weight: 900; font-size: 22px; letter-spacing: .5px; text-transform: uppercase; }
  .person__role { font-weight: 700; font-size: 13px; margin-top: 2px; }

  .company {
    position: absolute;
    right: 345px; top: 160px;
    text-align: right;
    font-weight: 900;
    font-size: 16px;
    line-height: 21px;
    white-space: nowrap;
  }
  .company__name { color: var(--orange); font-size: 17px; margin-bottom: 6px; }

  .divider {
    position: absolute;
    left: 318px; top: 140px;
    width: 3px; height: 140px;
    background: linear-gradient(to bottom, rgba(232,115,31,0), var(--orange) 40%, rgba(232,115,31,0));
  }
  .contacts {
    position: absolute;
    left: 340px; top: 150px;
    list-style: none;
    margin: 0; padding: 0;
    font-size: 15px;
    font-weight: 700;
    white-space: nowrap;
  }
  .contacts li { display: flex; align-items: center; height: 24px; }
  .contacts svg { width: 18px; height: 18px; margin-right: 8px; }
  .contacts .web { font-weight: 900; font-size: 16px; margin-top: 4px; }
</style>
</head>
<body>

<section class="card card--back">
  <svg class="card__bands" viewBox="0 0 640 366" aria-hidden="true">
    <rect x="0" y="348" width="640" height="18" fill="var(--slate)"/>
    <path d="M392,348 Q380,348 386,338 Q393,326 412,326 H640 V348 Z" fill="var(--orange)"/>
  </svg>
  <div class="wordmark">kV7</div>
  <div class="eshops">
    <div>www.pohodanoviny.sk</div>
    <div>www.relaxbrodeky.cz</div>
  </div>
  <div class="tagline">Online nákupy v pohodlí domova</div>
</section>

<section class="card card--front">
  <svg class="card__bands" viewBox="0 0 640 366" aria-hidden="true">
    <rect x="0" y="348" width="640" height="18" fill="var(--slate)"/>
    <path d="M392,348 Q380,348 386,338 Q393,326 412,326 H640 V348 Z" fill="var(--orange)"/>
  </svg>
  <div class="wordmark">kV7</div>

  <div class="person">
    <div class="person__name">Peter Hulka</div>
    <div class="person__role">MSC. / CEO</div>
  </div>

  <div class="company">
    <div class="company__name">KV7 S.R.O</div>
    <div>Brezovanská 742/3</div>
    <div>931 05 Lipová Dolina</div>
    <div>Central Europe (EU)</div>
  </div>

  <div class="divider"></div>

  <ul class="contacts">
    <li><svg viewBox="0 0 18 18"><circle cx="9" cy="9" r="9" fill="var(--slate)"/><rect x="6" y="4" width="6" height="10" rx="1" fill="none" stroke="#fff" stroke-width="1.3"/></svg>+421 (0) 907 251 836</li>
    <li><svg viewBox="0 0 18 18"><circle cx="9" cy="9" r="9" fill="var(--slate)"/><path d="M4,8 Q9,3 14,8 L12,9 L11,7.5 H7 L6,9 Z M5,10 H13 V13 H5 Z" fill="#fff"/></svg>+421 (0) 947 618 204</li>
    <li><svg viewBox="0 0 18 18"><circle cx="9" cy="9" r="9" fill="var(--slate)"/><rect x="4.5" y="5.5" width="9" height="7" fill="none" stroke="#fff" stroke-width="1.2"/><path d="M4.5,5.5 L9,9.5 L13.5,5.5" fill="none" stroke="#fff" stroke-width="1.2"/></svg>info@kv7example.sk</li>
    <li class="web">www.kv7example.sk</li>
  </ul>
</section>

</body>
</html>
```